Wedding Decor and Entertianment business card

Company - We run a weddings and events company called Amber Finch, we provide most entertainment and decor services to our customers.

Initial idea is ....
A simple business card with logo on the front, this will be spot varnish. On a matt black background.
The reverse will be simple contact information.

But happy to try things outside of the box and would welcome some crazy ideas.

Target Market(s)

wedding couples - 21 - 40
High end wedding venues.

Industry/Entity Type

Wedding

Contact Information for Business Card

01492 718 263
amberfinchevents.co.uk
rowan@amberfinchevents.co.uk
or
helena@amberfinchevents.co.uk

Requirements
Nice to have
• black matt background with spot varnish logo on the front.

```html
<!DOCTYPE html>
<html lang="en">
<head>
<meta charset="utf-8">
<title>Amber Finch – Business Card Front</title>
<link rel="stylesheet" href="https://fonts.googleapis.com/css2?family=Jost:wght@400&display=swap">
<style>
  :root {
    --card-black: #060708;
    --lace-grey: #34383b;
    --lace-fade: rgba(52, 56, 59, 0);
    --brand-purple: #7b3f9e;
    --mark-grey: #262b2f;
  }
  * { margin: 0; padding: 0; box-sizing: border-box; }
  html, body {
    width: 1200px;
    height: 686px;
    overflow: hidden;
    background: var(--card-black);
  }
  .card-front {
    position: relative;
    width: 1200px;
    height: 686px;
    background: var(--card-black);
    overflow: hidden;
  }
  .lace-corner {
    position: absolute;
    display: block;
  }
  .lace-corner--top-right {
    top: 0;
    right: 0;
    width: 620px;
    height: 300px;
  }
  .lace-corner--bottom-left {
    left: 0;
    bottom: 0;
    width: 410px;
    height: 170px;
  }
  .brand-lockup {
    position: absolute;
    left: 206px;
    top: 260px;
    height: 172px;
    display: flex;
    align-items: center;
    gap: 36px;
  }
  .brand-mark {
    width: 96px;
    height: 96px;
    border: 6px solid var(--mark-grey);
    border-radius: 50%;
    flex: none;
  }
  .brand-name {
    font-family: "Jost", "Futura", sans-serif;
    font-weight: 400;
    font-size: 43px;
    line-height: 1;
    letter-spacing: 0.72em;
    text-transform: uppercase;
    color: var(--brand-purple);
    white-space: nowrap;
  }
</style>
</head>
<body>
  <main class="card-front">
    <svg class="lace-corner lace-corner--top-right" viewBox="0 0 620 300" role="img" aria-label="Decorative lace flourish with flowers and paisley in the top right corner">
      <defs>
        <radialGradient id="laceTopGlow" cx="0.85" cy="0.3" r="0.75">
          <stop offset="0" stop-color="var(--lace-grey)" stop-opacity="0.9"/>
          <stop offset="1" stop-color="var(--lace-grey)" stop-opacity="0"/>
        </radialGradient>
      </defs>
      <path d="M0 0 H620 V300 C560 290 520 250 470 240 C410 225 380 160 300 110 C220 70 120 60 60 30 C30 18 10 8 0 0 Z" fill="url(#laceTopGlow)"/>
    </svg>

    <svg class="lace-corner lace-corner--bottom-left" viewBox="0 0 410 170" role="img" aria-label="Decorative lace flourish with scrolling leaves in the bottom left corner">
      <defs>
        <radialGradient id="laceBottomGlow" cx="0.15" cy="0.9" r="0.85">
          <stop offset="0" stop-color="var(--lace-grey)" stop-opacity="0.9"/>
          <stop offset="1" stop-color="var(--lace-grey)" stop-opacity="0"/>
        </radialGradient>
      </defs>
      <path d="M0 170 V10 C40 0 70 30 100 60 C150 100 230 110 300 130 C350 145 390 155 410 170 Z" fill="url(#laceBottomGlow)"/>
    </svg>

    <div class="brand-lockup">
      <span class="brand-mark" aria-hidden="true"></span>
      <h1 class="brand-name">Amber Finch</h1>
    </div>
  </main>
</body>
</html>
```